SUMMER 2017 WORK EXPERIENCE BROCHURE

We need an emailable PDF brochure with details of our Summer English Language and Work Experience Programmes in the UK. Our company is a family run business based in the South East of England, who pride themselves in personal attention to detail and delivering high quality Language Experiences to European students aged 16 plus. We would like the brochure to be bright, eye catching to both parents and older teenage students. It should contain our Company Blue and our logo.
Target Market(s)
European parents of teenage children interested in sending their children to the UK for English Language and Work Experience programmes
Industry/Entity Type
Travel Industry
Requirements
Must have
- Must be bright - eye catching and information must be easily readable. Must include company logo and have strong brand identity. Some images of teenage students having fun outdoors, doing sports, in learning environments. 2 pages. Must include schedule (see attached word document)
Nice to have
- Want it to show the fun element of the programme, it should feel summery and contain some images of beaches or ocean as we are based by the English seaside.
Should not have
- Should not be too conservative or boring. I have uploaded my previous brochure so you can see what type of thing I've had before - but I am looking for something very different to this :-) *** Have removed previous brochure as I am looking for something completely different, not a variation of the old one.

```html
<!DOCTYPE html>
<html lang="en">
<head>
<meta charset="utf-8">
<title>Summer 2017 Work Experience Brochure</title>
<link href="https://fonts.googleapis.com/css2?family=Lato:ital,wght@0,300;0,400;0,700;0,900;1,400;1,700&family=Oswald:wght@500;600&display=swap" rel="stylesheet">
<style>
:root{
  --stage:#3b3b3b;
  --brand-teal:#5cc6cf;
  --teal-dark:#3aa9b4;
  --teal-soft:#d8f3f5;
  --teal-mid:#a9e2e6;
  --orange:#f7941d;
  --orange-light:#fbb040;
  --ink:#2e2e2e;
  --grey-text:#444;
  --paper:#ffffff;
  --paper-warm:#f5f5f3;
}
*{box-sizing:border-box;margin:0;padding:0}
html,body{width:902px;height:1200px;overflow:hidden}
body{background:var(--stage);font-family:"Lato",sans-serif;color:var(--grey-text);position:relative}

.page-label{position:absolute;color:#fff;font-weight:700;font-size:18px}

.spread{position:absolute;width:697px;height:496px;background:var(--paper);overflow:hidden;box-shadow:0 8px 24px rgba(0,0,0,.5)}
.spread--outside{left:140px;top:81px}
.spread--inside{left:133px;top:637px}
.panel{position:absolute;top:0;height:496px;overflow:hidden}

.photo{position:absolute;display:block}
.pill{display:inline-block;background:var(--orange);color:#fff;font-weight:700;border-radius:10px;text-align:center}

/* company name: one colour, one weight, plain circle beside */
.company{display:flex;align-items:center;gap:6px}
.company-dot{width:10px;height:10px;border-radius:50%;background:var(--orange);flex:none}
.company-name{font-family:"Lato",sans-serif;font-weight:700;color:var(--ink);line-height:1.1;white-space:nowrap}

/* page 5 */
.panel--about{left:0;width:232px;background:var(--paper-warm)}
.about-photo{left:0;top:0;width:232px;height:104px;background:linear-gradient(160deg,#cfe3ea,#8aa48c 55%,#b7a58f)}
.about-pill{position:absolute;left:80px;top:104px;font-size:9px;padding:2px 10px;width:80px}
.about-text{position:absolute;left:16px;top:124px;width:202px;font-size:5.6px;line-height:1.38;text-align:justify;color:#333}
.director-photo{left:12px;top:250px;width:70px;height:70px;border-radius:50%;background:radial-gradient(#bdbdbd,#555);border:4px solid var(--brand-teal);box-shadow:0 0 0 2px #fff}
.director-name{position:absolute;left:112px;top:282px;font-size:8.5px;font-weight:700;color:var(--ink)}
.director-role{position:absolute;left:112px;top:293px;font-size:6px;color:#555}
.about-curve{position:absolute;left:0;top:310px;width:232px;height:186px}

/* back */
.panel--back{left:232px;width:232px}
.back-photo{left:0;top:0;width:232px;height:400px;background:linear-gradient(180deg,#d9eef3 0%,#9fd3e6 40%,#c7d9cf 72%,#e4d9bd 100%)}
.back-curve{position:absolute;left:0;top:330px;width:232px;height:166px}
.back-company{position:absolute;left:64px;top:50px;width:116px;height:44px;background:#fff;border:1.5px solid var(--brand-teal);border-radius:6px;justify-content:center}
.back-company .company-name{font-size:8.5px}
.map{left:6px;top:352px;width:52px;height:118px;border-radius:4px;background:linear-gradient(135deg,#eef0ea,#cfd9c9);border:2px solid #fff}
.contact{position:absolute;left:96px;top:402px;width:130px;font-size:6.3px;line-height:1.3;color:#333}
.contact li{list-style:none;display:flex;gap:5px;margin-bottom:5px}
.contact svg{flex:none;width:7px;height:7px;margin-top:1px}
.web-bar{position:absolute;left:0;bottom:0;width:232px;height:18px;background:linear-gradient(90deg,var(--orange),var(--orange-light));color:var(--ink);font-size:7.5px;font-weight:700;display:flex;align-items:center;justify-content:center;gap:5px}
.web-bar i{width:6px;height:6px;border-radius:50%;background:#fff;display:inline-block}

/* front */
.panel--front{left:464px;width:233px}
.front-photo{left:0;top:0;width:233px;height:300px;background:linear-gradient(180deg,#bfe3f0 0%,#8fcbe2 45%,#d9c7ad 100%)}
.front-curve{position:absolute;left:0;top:220px;width:233px;height:276px}
.front-company{position:absolute;left:0;width:233px;top:300px;justify-content:center}
.front-company .company-dot{width:14px;height:14px}
.front-company .company-name{font-size:14px}
.front-title{position:absolute;right:16px;top:386px;text-align:right;font-weight:900;line-height:1}
.front-title .t-summer{font-size:24px;color:var(--ink);letter-spacing:.5px}
.front-title .t-year{font-size:40px;color:#fff;letter-spacing:1px}
.front-title .t-work{font-size:19px;color:var(--ink);margin-top:2px}

/* page 2 */
.panel--programme{left:0;width:245px;background:var(--paper-warm)}
.prog-head{position:absolute;left:0;width:245px;top:24px;justify-content:center}
.prog-head .company-name{font-size:9px}
.prog-body{position:absolute;left:14px;top:54px;width:220px;font-size:5.8px;line-height:1.35;color:#333}
.prog-body .pill{font-size:7px;padding:1px 8px;margin:0 0 4px 44px;width:118px}
.prog-body .pill--short{margin-left:60px;width:80px}
.prog-body p{margin-bottom:3px}
.prog-body ul{margin:2px 0 5px 0}
.prog-body li{list-style:none;position:relative;padding-left:9px;font-style:italic;font-weight:700;margin-bottom:2px}
.prog-body li::before{content:"";position:absolute;left:0;top:1.5px;width:4px;height:4px;border-radius:50%;background:var(--orange)}
.note-orange{color:var(--orange);font-style:italic;font-weight:700}
.plan-bar{position:absolute;left:0;width:245px;height:20px;background:linear-gradient(90deg,var(--brand-teal),#8ad8de);display:flex;align-items:center;justify-content:space-between;padding:0 12px 0 14px}
.plan-bar h2{font-family:"Oswald",sans-serif;font-weight:600;font-size:10.5px;color:#fff}
.price{background:var(--orange);color:#fff;font-family:"Oswald",sans-serif;font-weight:600;font-size:10px;padding:2px 6px;border-radius:3px;border:1.5px solid #fff}
.plan-bar--two{top:238px}
.plan-bar--four{top:358px}
.plan-list{position:absolute;left:14px;width:222px;font-size:5.5px;line-height:1.3;color:#333}
.plan-list--two{top:264px}
.plan-list--four{top:384px}
.plan-list p{font-weight:700;margin-bottom:4px;font-size:6px}
.plan-list p span{color:var(--orange);font-weight:400}
.plan-list li{list-style:none;position:relative;padding-left:9px;font-style:italic;font-weight:700;margin-bottom:3px}
.plan-list li::before{content:"";position:absolute;left:0;top:1px;width:4px;height:4px;border-radius:50%;background:var(--orange)}
.plan-list .footnote{color:var(--orange);font-style:italic;font-weight:400;font-size:5px;margin-left:9px}

/* schedule */
.panel--schedule{left:245px;width:452px;background:#fff}
.week{position:absolute;left:2px;width:448px;border:1px solid #bfe6e9;border-radius:6px;overflow:hidden;background:#fff}
.week--1{top:12px}.week--2{top:110px}.week--3{top:207px}.week--4{top:304px}
.week-head{height:12px;background:linear-gradient(90deg,var(--orange),var(--orange-light));position:relative}
.week-head h3{position:absolute;left:0;top:0;width:102px;height:12px;background:var(--teal-mid);color:var(--ink);font-size:7px;font-weight:700;padding:2px 0 0 8px;border-radius:0 0 8px 0}
.schedule{width:100%;border-collapse:separate;border-spacing:1px;table-layout:fixed;font-size:5px;color:#333}
.schedule th{font-weight:700;font-size:6px;height:10px;color:var(--ink)}
.schedule th:first-child{width:44px}
.schedule td{background:var(--teal-soft);height:22px;vertical-align:top;padding:2px 3px;line-height:1.2}
.schedule td.slot{background:var(--brand-teal);color:#fff;font-weight:700;font-size:6px;vertical-align:middle;text-align:center}
.schedule td.deep{background:var(--teal-mid)}
.schedule tr.eve td{height:14px}
.schedule td.blank{background:#eafafb}
.desk-photo{left:0;top:400px;width:165px;height:96px;background:linear-gradient(135deg,#e9e4dc,#c8b9a4 50%,#6f8fa3)}
.schedule-pill{position:absolute;left:176px;top:404px;font-size:8px;padding:1px 10px;width:70px}
.schedule-text{position:absolute;left:176px;top:420px;width:266px;font-size:5.5px;line-height:1.38;text-align:justify;color:#333}
.fold{position:absolute;top:0;width:1px;height:496px;background:rgba(0,0,0,.08)}
</style>
</head>
<body>

<span class="page-label" style="left:158px;top:24px">Page 5</span>
<span class="page-label" style="left:416px;top:24px">Back</span>
<span class="page-label" style="left:668px;top:24px">Front</span>

<section class="spread spread--outside">
  <div class="panel panel--about">
    <div class="photo about-photo" role="img" aria-label="Photo of teenage students cycling together on a sunny street"></div>
    <span class="pill about-pill">ABOUT US</span>
    <p class="about-text">Saltmarsh Study Travel Ltd is a friendly, family run business, based in Seabrook, West Sussex. We pride ourselves in offering bespoke English Language Experiences to children of all ages and nationalities, as well as their parents! We work with a select number of partners in both the UK and Europe to provide a wide range of English Language Programme options for European students, exciting activities and a full and varied social programme. What our clients tell us they like most about Saltmarsh Study Travel Ltd is the personal attention to detail they receive before, during and after their UK English Language Experiences. We take great care to ensure that each student receives the best experience possible, on an individual basis, starting with accompanied group travel from their country of origin, where appropriate. Saltmarsh Study Travel is a registered Limited Company and has full Tour Operator's Liability and Public Liability Insurance. We look forward to welcoming you to Seabrook very soon!</p>
    <div class="photo director-photo" role="img" aria-label="Portrait photo of the company director"></div>
    <span class="director-name">Morgan Ashby-Hale</span>
    <span class="director-role">Director</span>
    <svg class="about-curve" viewBox="0 0 232 186" aria-hidden="true">
      <defs><linearGradient id="beachGroup" x1="0" y1="0" x2="0" y2="1"><stop offset="0" stop-color="#9fd6ea"/><stop offset=".6" stop-color="#d9b99a"/><stop offset="1" stop-color="#4a4a4a"/></linearGradient></defs>
      <path d="M0 40 Q110 6 232 14 L232 186 L0 186Z" fill="var(--brand-teal)"/>
      <path d="M0 46 Q110 14 232 22 L232 186 L0 186Z" fill="var(--orange)"/>
      <path d="M0 52 Q110 22 232 30 L232 186 L0 186Z" fill="url(#beachGroup)" role="img" aria-label="Photo of happy teenagers on a beach, framed on a phone screen"/>
    </svg>
  </div>

  <div class="panel panel--back">
    <div class="photo back-photo" role="img" aria-label="Photo of a group of young people laughing on a sunny beach"></div>
    <div class="company back-company">
      <span class="company-dot"></span>
      <span class="company-name">Saltmarsh Study Travel</span>
    </div>
    <svg class="back-curve" viewBox="0 0 232 166" aria-hidden="true">
      <defs><linearGradient id="backFade" x1="0" y1="0" x2="0" y2="1"><stop offset="0" stop-color="#bfeef1"/><stop offset="1" stop-color="#f2fcfd"/></linearGradient></defs>
      <path d="M0 0 Q60 70 232 40 L232 166 L0 166Z" fill="var(--brand-teal)"/>
      <path d="M0 14 Q70 80 232 52 L232 166 L0 166Z" fill="url(#backFade)"/>
    </svg>
    <div class="photo map" role="img" aria-label="Street map showing the office location"></div>
    <ul class="contact">
      <li><svg viewBox="0 0 10 10"><path d="M5 0a3.5 3.5 0 0 1 3.5 3.5C8.5 6 5 10 5 10S1.5 6 1.5 3.5A3.5 3.5 0 0 1 5 0z" fill="var(--orange)"/><circle cx="5" cy="3.5" r="1.3" fill="#fff"/></svg><span>Quay House, Marina Walk,<br>Seabrook, West Sussex,<br>BN00 1AA</span></li>
      <li><svg viewBox="0 0 10 10"><path d="M2 0.5l2 2-1 1.5c.6 1.3 1.6 2.3 2.9 2.9l1.5-1 2 2L8 9.5C4 9.5.5 6 .5 2z" fill="var(--orange)"/></svg><span>+44 (0)7000 123456</span></li>
      <li><svg viewBox="0 0 10 10"><path d="M2 0.5l2 2-1 1.5c.6 1.3 1.6 2.3 2.9 2.9l1.5-1 2 2L8 9.5C4 9.5.5 6 .5 2z" fill="var(--orange)"/></svg><span>+44 (0)1000 654321</span></li>
      <li><svg viewBox="0 0 10 10"><rect x=".5" y="2" width="9" height="6.5" fill="var(--orange)"/><path d="M.5 2l4.5 3.5L9.5 2" stroke="#fff" stroke-width=".8" fill="none"/></svg><span>info@saltmarshstudy.com</span></li>
    </ul>
    <div class="web-bar"><i></i>www.saltmarshstudy.com</div>
  </div>

  <div class="panel panel--front">
    <div class="photo front-photo" role="img" aria-label="Photo of teenagers playing volleyball on the beach under a blue sky"></div>
    <svg class="front-curve" viewBox="0 0 233 276" aria-hidden="true">
      <defs>
        <linearGradient id="frontSun" x1="0" y1="0" x2="1" y2="1"><stop offset="0" stop-color="#fbb040"/><stop offset="1" stop-color="#f47b20"/></linearGradient>
        <linearGradient id="frontWhite" x1="0" y1="0" x2="0" y2="1"><stop offset="0" stop-color="#fff"/><stop offset="1" stop-color="#eaf7f8"/></linearGradient>
      </defs>
      <path d="M0 70 Q120 20 233 0 L233 276 L0 276Z" fill="var(--orange)"/>
      <path d="M0 80 Q120 32 233 14 L233 276 L0 276Z" fill="url(#frontWhite)"/>
      <path d="M0 210 Q90 150 233 140 L233 276 L0 276Z" fill="var(--brand-teal)"/>
      <path d="M0 222 Q90 162 233 152 L233 276 L0 276Z" fill="#fff"/>
      <path d="M0 228 Q90 170 233 160 L233 276 L0 276Z" fill="url(#frontSun)"/>
    </svg>
    <div class="company front-company">
      <span class="company-dot"></span>
      <span class="company-name">Saltmarsh Study Travel</span>
    </div>
    <div class="front-title">
      <div class="t-summer">SUMMER</div>
      <div class="t-year">2017</div>
      <div class="t-work">WORK EXPERIENCE</div>
    </div>
  </div>
  <span class="fold" style="left:232px"></span>
  <span class="fold" style="left:464px"></span>
</section>

<section class="spread spread--inside">
  <div class="panel panel--programme">
    <div class="company prog-head">
      <span class="company-dot"></span>
      <span class="company-name">Work Experience Programme</span>
    </div>
    <div class="prog-body">
      <span class="pill">Work Experience Programme</span>
      <p><b>2 or 4 week placements</b> - Longer placements available on request<br>Ages from 16yrs+ available all year.</p>
      <p><b>All Internships</b> - Host family shared accommodation to include all meals and light laundry.</p>
      <span class="pill pill--short">Eligibility criteria</span>
      <ul>
        <li>Hold EU Nationality</li>
        <li>Have a minimum level of Intermediate English (B1 or B2)</li>
        <li>Must be looking for a minimum of 2 week placement in a professional working environment</li>
      </ul>
      <p>Saltmarsh Study Travel offers internships in the following sectors: Hotel and Catering trade, Retail Sales, Travel and Tourism, PR (Public Relations), Design, Fashion, Art, photo &amp; print galleries, Marketing, Voluntary and Charitable Sectors, Media</p>
      <p class="note-orange">The following are only available to students 18yrs plus:</p>
      <p>Secretarial and/or translation, Journalism, Administration International Trade, Architecture, Electrical &amp; engineering Law, IT</p>
    </div>

    <div class="plan-bar plan-bar--two"><h2>2 WEEK PROGRAMME</h2><span class="price">UK£1,525</span></div>
    <div class="plan-list plan-list--two">
      <p>For UK£1,525 <span>( UK£118 per day)</span> you get:</p>
      <ul>
        <li>A chaperone from/to your country of origin to travel with the student.</li>
        <li>Private return UK airport transfers.</li>
        <li>13 nights host family shared accommodation, including 3 meals per day and light laundry.</li>
        <li>Work Experience Placement fee including workplace insurance.</li>
        <li>2 week travel card to/from work.</li>
        <li>2 week social programme including 2 nights 'glamping' and tree climbing experience.</li>
        <li>24hr on site assistance including private medical assistance.</li>
      </ul>
    </div>

    <div class="plan-bar plan-bar--four"><h2>4 WEEK PROGRAMME</h2><span class="price">UK£1,800</span></div>
    <div class="plan-list plan-list--four">
      <p>For £1,800 <span>(UK£ 66.00 per day)</span> you get:</p>
      <ul>
        <li>A chaperone from/to your country of origin to travel with the student.</li>
        <li>Private return UK airport transfers.</li>
        <li>27 nights host family shared accommodation, including 3 meals per day and light laundry.</li>
        <li>Work Experience Placement fee including workplace insurance.</li>
        <li>4 week travel card to/from work.</li>
        <li>4 week social programme including 2 nights 'glamping' and tree climbing experience.</li>
        <li>24hr on site assistance including private medical assistance.</li>
      </ul>
      <span class="footnote">*subject to a minimum of 10 students per group</span>
    </div>
  </div>

  <div class="panel panel--schedule">
    <div class="week week--1">
      <div class="week-head"><h3>WEEK 1</h3></div>
      <table class="schedule">
        <tr><th></th><th>Sunday</th><th>Monday</th><th>Tuesday</th><th>Wednesday</th><th>Thursday</th><th>Friday</th><th>Saturday</th></tr>
        <tr><td class="slot">AM</td><td rowspan="2">Arrivals at London Gatwick Airport</td><td class="deep">Induction Meeting followed by Work Placements</td><td>Work Placements</td><td class="deep">Work Placements</td><td>Work Placements</td><td>Work Placements</td><td rowspan="2">Camping and Tree Climbing Experience</td></tr>
        <tr><td class="slot">PM</td><td class="deep">Work Placements</td><td>Work Placements</td><td class="deep">Work Placements</td><td>Work Placements</td><td>Transfer to camp site</td></tr>
        <tr class="eve"><td class="slot">Evening</td><td class="blank"></td><td class="deep"></td><td>Evening activity</td><td class="deep"></td><td>Evening activity</td><td>Overnight at campsite</td><td class="blank"></td></tr>
      </table>
    </div>

    <div class="week week--2">
      <div class="week-head"><h3>WEEK 2</h3></div>
      <table class="schedule">
        <tr><th></th><th>Sunday</th><th>Monday</th><th>Tuesday</th><th>Wednesday</th><th>Thursday</th><th>Friday</th><th>Saturday</th></tr>
        <tr><td class="slot">AM</td><td rowspan="2">Camping and transfers back to Seabrook</td><td class="deep">Work Placements</td><td>Work Placements</td><td class="deep">Work Placements</td><td>Work Placements</td><td>Work Placements</td><td rowspan="2">Day Trip to London</td></tr>
        <tr><td class="slot">PM</td><td class="deep">Work Placements</td><td>Work Placements</td><td class="deep">Work Placements</td><td>Work Placements</td><td>Afternoon activity</td></tr>
        <tr class="eve"><td class="slot">Evening</td><td class="blank"></td><td class="deep"></td><td>Evening activity</td><td class="deep"></td><td>Evening activity</td><td></td><td class="blank"></td></tr>
      </table>
    </div>

    <div class="week week--3">
      <div class="week-head"><h3>WEEK 3</h3></div>
      <table class="schedule">
        <tr><th></th><th>Sunday</th><th>Monday</th><th>Tuesday</th><th>Wednesday</th><th>Thursday</th><th>Friday</th><th>Saturday</th></tr>
        <tr><td class="slot">AM</td><td rowspan="2">Free day</td><td class="deep">Work Placements</td><td>Work Placements</td><td class="deep">Work Placements</td><td>Work Placements</td><td>Work Placements</td><td rowspan="2">Day Trip to Portsmouth</td></tr>
        <tr><td class="slot">PM</td><td class="deep">Work Placements</td><td>Work Placements</td><td class="deep">Work Placements</td><td>Work Placements</td><td>Afternoon activity</td></tr>
        <tr class="eve"><td class="slot">Evening</td><td class="blank"></td><td class="deep"></td><td>Evening activity</td><td class="deep"></td><td>Evening activity</td><td></td><td class="blank"></td></tr>
      </table>
    </div>

    <div class="week week--4">
      <div class="week-head"><h3>WEEK 4</h3></div>
      <table class="schedule">
        <tr><th></th><th>Sunday</th><th>Monday</th><th>Tuesday</th><th>Wednesday</th><th>Thursday</th><th>Friday</th><th>Saturday</th></tr>
        <tr><td class="slot">AM</td><td rowspan="2">Free day</td><td class="deep">Work Placements</td><td>Work Placements</td><td class="deep">Work Placements</td><td>Work Placements</td><td>Work Placements</td><td rowspan="2">Departures</td></tr>
        <tr><td class="slot">PM</td><td class="deep">Work Placements</td><td>Work Placements</td><td class="deep">Work Placements</td><td>Work Placements</td><td>Certificate presentations</td></tr>
        <tr class="eve"><td class="slot">Evening</td><td class="blank"></td><td class="deep"></td><td>Evening activity</td><td class="deep"></td><td>Evening activity</td><td></td><td class="blank"></td></tr>
      </table>
    </div>

    <div class="photo desk-photo" role="img" aria-label="Photo of a smiling student working at an office desk"></div>
    <span class="pill schedule-pill">SCHEDULE</span>
    <p class="schedule-text">Saltmarsh Study Travel is a family run business. We offer far more than just a Work Experience Programme; we offer a full immersion experience that is educational, fun, motivating and safe. Students are placed in real-life working environments in a structured and professional programme which is mentored and regularly monitored to ensure that each individual student gets the best possible exposure to their business sector of interest during their time in the UK. Our programmes are designed to make their stay beneficial, interesting and above all memorable. Students will come away from their UK Work Experience Programme with better understanding of the workplace enabling them to make more informed decisions about life after school.</p>
  </div>
  <span class="fold" style="left:245px"></span>
  <span class="fold" style="left:471px"></span>
</section>

<span class="page-label" style="left:176px;top:1165px">Page 2</span>
<span class="page-label" style="left:436px;top:1160px">Page 3</span>
<span class="page-label" style="left:690px;top:1165px">Page 4</span>

</body>
</html>
```